Design Brief for Website Redesign

Client Name: Velmora IT
Website: www.velmorait.com.au
Industry: Managed IT Services
Target Audience: Small to medium-sized businesses in Australia, requiring IT solutions, IT support, cloud services, and phone systems.

Project Overview
We are seeking a full redesign of the Velmora IT website to modernize its look, improve usability, and enhance user experience across devices. The goal is to create a professional, clean, and user-friendly website that reflects our expertise in IT services and appeals to our business clients.

Objectives
Modern Visual Identity: Create a fresh, modern design that aligns with Velmora IT's branding.

Improved User Experience: Simplify navigation, improve accessibility, and enhance mobile responsiveness.

Clear Calls to Action: Ensure CTAs are prominent and encourage user engagement.

Enhanced Trust & Credibility: Highlight testimonials, case studies, and industry credentials.

SEO Optimization: Ensure the site is optimized for search engines, including proper heading structures and metadata.
Design Style & Tone
Professional: Clean, modern, and polished to reflect our IT expertise.

Minimalist: Simple layouts, plenty of white space, and easy-to-read typography.

Tech-focused: Subtle tech-themed design elements that reinforce our brand as a leading IT service provider.

Colors: Use our existing brand colors, or propose a color scheme that complements the tech industry while maintaining a professional feel.

Typography: Clear, readable fonts that convey professionalism and trustworthiness.

Key Pages & Features
Home Page:

Hero section with a clear value proposition.

Highlight key services (IT support, cloud solutions, phone systems, etc.) with icons and brief descriptions.

Prominent CTAs (e.g., “Request a Quote,” “Book a Demo”).

Testimonials from satisfied clients.

Services Page:

Detailed breakdown of the services we offer (IT support, cloud services, phone systems, etc.).

Use of icons or illustrations to make the services visually engaging.

Clear CTAs to request quotes or book consultations.

About Us Page:

Information about our company history, mission, and team.

Highlight our certifications, partnerships, and industry expertise.

Case Studies/Testimonials Page:

Showcase client success stories and testimonials with visuals and brief case study summaries.

Include a trust-building section with logos of major clients or partners.

Contact Page:

Simple contact form for inquiries.

Integrated map with office location.

Social media links and phone number.

Blog/Resource Section:

Easy-to-navigate blog section for IT-related articles, tips, and industry news.

Clear categorization and tags for easy browsing.

Knowledge Base/Support Page:

Self-service area for clients to find articles, FAQs, and support guides.

Option to submit a support ticket.

Mobile Responsiveness:

Ensure the design is fully responsive, with no horizontal scrolling or misaligned content on mobile.

Functional Requirements
Fast Load Times: Optimize images, minimize unnecessary scripts, and ensure the site loads quickly on both desktop and mobile.

User-Friendly CMS: We need a CMS that is easy to update (preferably WordPress, but open to other suggestions).

SEO Best Practices: Structure the site with proper metadata, alt tags, and semantic HTML for better search engine optimization.

Security: Ensure the website follows security best practices (SSL, HTTPS).

Deliverables
Full website design (desktop and mobile versions).

Design mockups in Photoshop, Sketch, or Figma (whichever is preferred).

Working prototype (optional).

Final website files, including images and assets.

A style guide for ongoing consistency.

Industry/Entity Type

IT Managed Services

Number of Pages Required

3 page

Requirements
Must have
• EXCELLENT UX/UI

```html
<!DOCTYPE html>
<html lang="en">
<head>
<meta charset="utf-8">
<title>Velmora IT – Technology Solutions for Better Business</title>
<link rel="stylesheet" href="https://fonts.googleapis.com/css2?family=Exo+2:wght@600;700&family=Poppins:wght@400;500;600;700&display=swap">
<style>
:root{
  --navy:#0d2340;
  --navy-deep:#0a1c33;
  --red:#ec1c3a;
  --red-soft:#f5334f;
  --ink:#14233a;
  --muted:#6b7280;
  --line:#e5e7eb;
  --white:#ffffff;
}
*{box-sizing:border-box;margin:0;padding:0}
html,body{width:1200px;height:4658px;overflow:hidden}
body{font-family:"Poppins",sans-serif;color:var(--ink);background:var(--white);position:relative}
.heading{font-family:"Exo 2",sans-serif;font-weight:700}
.accent{color:var(--red)}
.abs{position:absolute}
.btn{display:inline-block;border-radius:30px;font-size:12px;font-weight:700;text-transform:uppercase;text-align:center;line-height:42px;height:42px;color:var(--white);background:var(--red);text-decoration:none}
.btn-dark{background:#1d3556}

/* hero */
.hero{position:absolute;left:0;top:0;width:1200px;height:760px;background:var(--navy)}
.brand{font-family:"Exo 2",sans-serif;font-weight:700;color:var(--red);font-size:42px;letter-spacing:1px}
.nav{position:absolute;left:360px;top:34px;display:flex;gap:18px;font-size:11px;font-weight:500;color:var(--white);text-transform:uppercase;line-height:18px}
.nav-cta{position:absolute;left:937px;top:22px;width:174px}
.hero-map{position:absolute;left:540px;top:60px;width:660px;height:540px;background:radial-gradient(ellipse at 55% 45%,#b3162d 0%,#6d1428 35%,rgba(13,35,64,0) 70%)}
.hero h1{position:absolute;left:89px;top:258px;font-size:47px;line-height:54px;color:var(--white)}
.hero p{position:absolute;left:89px;top:384px;width:480px;font-size:14px;line-height:23px;color:#d5dce6}
.counter{position:absolute;left:1058px;top:578px;color:var(--white);font-family:"Exo 2",sans-serif;font-weight:700;font-size:44px}
.counter small{font-size:18px}
.mouse{position:absolute;left:89px;top:611px;width:68px;height:68px;border-radius:50%;background:#22395a}

/* about */
.about{position:absolute;left:0;top:660px;width:1200px;height:1060px;background:var(--white);border-top-left-radius:200px}
.photo{position:absolute;left:137px;top:108px;width:435px;height:470px;border-radius:8px;background:linear-gradient(135deg,#c9d3df,#8ea0b6 60%,#e8ecf1)}
.about h2{position:absolute;left:625px;top:160px;font-size:30px;line-height:37px}
.sub{font-size:13.5px;font-weight:600}
.body{font-size:13.5px;line-height:23px;color:var(--muted)}

/* why */
.card{position:absolute;top:645px;width:290px;height:368px;background:var(--white);border-radius:10px;box-shadow:0 8px 30px rgba(13,35,64,.12);text-align:center;padding:30px 22px}
.card .icon{width:88px;height:88px;border-radius:8px;margin:0 auto 24px;display:flex;align-items:center;justify-content:center}
.card h3{font-size:17px;margin-bottom:14px}
.card p{font-size:13px;line-height:23px;color:var(--muted)}
.card a{display:block;margin-top:12px;font-size:11px;font-weight:700;color:var(--red);text-decoration:underline}

/* services band */
.band{position:absolute;left:0;top:1756px;width:1200px;height:458px;background:var(--red-soft);border-top-left-radius:200px}
.band h2{position:absolute;left:0;width:1200px;top:64px;text-align:center;color:var(--white);font-size:30px;line-height:37px}
.band p{position:absolute;left:0;width:1200px;top:146px;text-align:center;color:#ffe7ea;font-size:13.5px;line-height:23px}
.svc{position:absolute;left:163px;top:1977px;width:874px;height:432px;background:var(--navy);border-radius:14px;padding:14px 60px 0 38px}
.svc-row{display:flex;align-items:center;border-bottom:1px solid #2a4266;height:73px}
.svc-row:last-child{border-bottom:0;height:100px}
.svc-row h4{width:260px;color:var(--white);font-size:15px;font-weight:600}
.svc-row h4::before{content:"";display:inline-block;width:6px;height:6px;border-radius:50%;background:var(--red);margin-right:8px;vertical-align:middle}
.svc-row p{flex:1;color:#d5dce6;font-size:13px;line-height:23px}
.svc-bar{position:absolute;right:30px;top:28px;width:6px;height:80px;background:var(--red);border-radius:3px}

/* testimonial */
.quote-mark{position:absolute;left:150px;top:2370px;font-family:"Exo 2",sans-serif;font-weight:700;font-size:560px;line-height:560px;color:#10305a}
.testi h2{position:absolute;left:594px;top:2518px;font-size:28px}
.testi p{position:absolute;left:594px;top:2575px;width:430px}
.testi .rule{position:absolute;left:594px;top:2737px;width:445px;height:1px;background:var(--line)}
.client{position:absolute;left:594px;top:2759px;height:42px;padding:0 14px;border:2px solid var(--ink);border-radius:4px;font-weight:700;font-size:15px;line-height:38px}
.arrows{position:absolute;display:flex;gap:14px}

/* customers */
.customers h2{position:absolute;left:0;width:1200px;top:2896px;text-align:center;font-size:29px}
.logos{position:absolute;left:108px;top:2965px;display:flex;gap:9px}
.logo-box{width:191px;height:80px;border:2px solid #4a7fc1;border-radius:6px;background:var(--white);box-shadow:0 4px 14px rgba(13,35,64,.1);display:flex;align-items:center;justify-content:center;font-size:22px;font-weight:700;color:var(--ink)}
.logo-box.red{border-color:var(--red)}

/* resources */
.res h2{position:absolute;left:0;width:1200px;top:3150px;text-align:center;font-size:30px}
.post{position:absolute;top:3222px;width:280px;height:405px;background:var(--white);border-radius:8px;box-shadow:0 6px 24px rgba(13,35,64,.12);overflow:hidden}
.post .thumb{height:205px}
.post .txt{padding:20px 24px}
.post time{display:block;font-size:11px;font-weight:600;color:var(--red);margin-bottom:12px}
.post h3{font-size:12.5px;line-height:19px;font-weight:600;margin-bottom:8px}
.post p{font-size:11.5px;line-height:18px;color:var(--muted)}
.post a{display:block;margin-top:10px;font-size:11.5px;font-weight:700;color:var(--red);text-decoration:underline}

/* contact */
.contact h2{position:absolute;left:123px;top:3854px;font-size:30px;line-height:40px}
.contact p{position:absolute;left:123px;top:4004px;width:480px}
.form{position:absolute;left:669px;top:3777px;width:406px;height:461px;background:var(--red);border-radius:22px;padding:30px 46px;z-index:2}
.form h3{text-align:center;color:var(--white);font-size:29px;margin-bottom:20px}
.field{height:38px;background:var(--white);border-radius:19px;margin-bottom:12px;font-size:11px;color:#555;padding-left:22px;line-height:38px}
.field.area{height:100px;border-radius:14px}
.submit{height:38px;border-radius:19px;background:var(--navy);color:var(--white);font-size:13px;font-weight:700;text-align:center;line-height:38px;margin-top:12px}

/* footer */
.footer{position:absolute;left:0;top:4178px;width:1200px;height:480px;background:var(--navy)}
.footer .brand{position:absolute;left:163px;top:150px;font-size:56px}
.socials{position:absolute;left:199px;top:237px;display:flex;gap:10px}
.socials span{width:36px;height:36px;border-radius:50%;background:#1f3a5f}
.fcol{position:absolute;top:140px;color:var(--white)}
.fcol h4{font-size:17px;font-weight:600;margin-bottom:14px}
.fcol li{list-style:none;font-size:12.5px;line-height:22px;color:#d5dce6}
.frule{position:absolute;left:89px;top:422px;width:1022px;height:1px;background:#2a4266}
.copy{position:absolute;left:0;width:1200px;top:440px;text-align:center;color:var(--white);font-size:12px;font-weight:600}
.top-btn{position:absolute;left:1138px;top:392px;width:40px;height:40px;border-radius:50%;background:var(--red)}
</style>
</head>
<body>

<header class="hero">
  <div class="hero-map" role="img" aria-label="Red world map with glowing network connection points"></div>
  <div class="abs brand" style="left:89px;top:8px">velmora</div>
  <nav class="nav">
    <span>Our Services</span><span>Huddle Chat</span><span>Partners</span><span>Remote</span><span>Resources</span><span>About</span><span>Shop</span><span>Contact</span>
  </nav>
  <a class="btn nav-cta">Request a Quote</a>
  <h1 class="heading">Technology Solutions<br>for better business</h1>
  <p>We understand that technology is a critical component of running a successful business, and that's why we're here to help you navigate the ever-changing landscape of IT.</p>
  <a class="btn abs" style="left:89px;top:480px;width:145px">Get a Quote</a>
  <a class="btn btn-dark abs" style="left:244px;top:480px;width:196px">View All Services</a>
  <div class="counter">01<small> /04</small></div>
  <div class="mouse">
    <svg width="68" height="68" viewBox="0 0 68 68"><rect x="27" y="21" width="14" height="24" rx="7" fill="none" stroke="#fff" stroke-width="2"/><line x1="34" y1="27" x2="34" y2="32" stroke="#fff" stroke-width="2"/></svg>
  </div>
</header>

<section class="about">
  <div class="photo" role="img" aria-label="Smiling help desk staff wearing headsets at a computer"></div>
  <h2 class="heading">Innovative <span class="accent">Technology<br>Solutions</span> for Better Business:</h2>
  <div class="abs sub" style="left:628px;top:250px">Your Managed IT Services Provider in Sydney</div>
  <div class="abs sub" style="left:628px;top:282px">Your Trusted IT Company for Managed IT Services Sydney</div>
  <p class="abs body" style="left:628px;top:314px;width:430px">We're Velmora IT, a Managed IT Services in Sydney provider. We offer expert IT Solutions and Support for Small and Medium Businesses.</p>
  <p class="abs body" style="left:628px;top:396px;width:430px">We are committed to listening to you, understanding your business needs, and providing IT Strategy and Support that aligns with your company's culture and bottom line</p>
  <a class="btn abs" style="left:628px;top:486px;width:145px">Get a Quote</a>

  <h2 class="heading abs" style="left:89px;top:742px;font-size:30px;line-height:37px">Why Velmora IT? <span class="accent">We<br>Think Ahead</span>, with You in Mind.</h2>
  <p class="abs body" style="left:89px;top:830px;width:480px">Whether you need a full-service IT Solution or just a little extra help, we have flexible service plans that can be tailored to the specific needs of your business.</p>
  <a class="btn abs" style="left:89px;top:918px;width:184px">View All Services</a>

  <div class="card" style="left:625px">
    <div class="icon" style="background:var(--red)">
      <svg width="48" height="48" viewBox="0 0 48 48" fill="none" stroke="#fff" stroke-width="2"><rect x="14" y="14" width="20" height="20" rx="3"/><path d="M19 8v6M24 8v6M29 8v6M19 34v6M24 34v6M29 34v6M8 19h6M8 24h6M8 29h6M34 19h6M34 24h6M34 29h6"/></svg>
    </div>
    <h3>Reliable IT Support</h3>
    <p>Our certified systems engineers have deep expertise and experience that spans many different products, industries, applications, and their unique challenges.</p>
    <a>Learn More</a>
  </div>
  <div class="card" style="left:937px">
    <div class="icon" style="background:var(--navy)">
      <svg width="48" height="48" viewBox="0 0 48 48" fill="none" stroke="#fff" stroke-width="2"><path d="M24 10l11 5v8c0 7-5 12-11 15-6-3-11-8-11-15v-8z"/><rect x="19" y="22" width="10" height="8" rx="1"/><path d="M21 22v-3a3 3 0 0 1 6 0v3"/></svg>
    </div>
    <h3>Robust Cyber Security</h3>
    <p>With a proactive approach to cybersecurity, we work behind the scenes to defend your business from evolving cyber threats. Our security measures ensure your business...</p>
    <a>Learn More</a>
  </div>
</section>

<section class="band">
  <h2 class="heading">Providing Cutting-Edge IT Solutions to<br>Mid-Market Sydney Businesses</h2>
  <p>We can provide for all of your IT needs and keep your systems running smoothly, securely,<br>and efficiently. Our services include:</p>
</section>
<div class="svc">
  <div class="svc-bar"></div>
  <div class="svc-row"><h4>Proactive Monitoring</h4><p>24 hr monitoring of your network and systems to detect and resolve issues before they become problems.</p></div>
  <div class="svc-row"><h4>Help Desk Support</h4><p>You and your team have access to our service desk, where IT experts are available to quickly assist you with any technical IT issues.</p></div>
  <div class="svc-row"><h4>Data Security</h4><p>Security solutions including firewalls, antivirus software, anti-malware software, email spam filtering, and intrusion detection systems.</p></div>
  <div class="svc-row"><h4>Disaster Recovery</h4><p>Backup and recovery solutions to keep your data safe and reduce downtime in the event of a disaster.</p></div>
  <div class="svc-row"><h4>IT Consulting</h4><p>Make the most of technology with expert advice and guidance on IT best practices. We will work with you to build a customised IT plan that makes IT a strategic advantage for your business.</p></div>
</div>

<section class="testi">
  <div class="quote-mark" aria-hidden="true">“</div>
  <h2 class="heading">What Our Clients Say</h2>
  <p class="body">The guys at Velmora IT were fantastic to deal with when helping us build our website from scratch. They helped us with everything from the marketing strategy, the colour scheme, the design &amp; the logo. We are very impressed with the outcome and highly recommend them.</p>
  <div class="rule"></div>
  <div class="client">Brightline Hardware</div>
  <div class="arrows" style="left:964px;top:2768px">
    <svg width="24" height="14" viewBox="0 0 24 14"><path d="M23 7H2M8 1L2 7l6 6" fill="none" stroke="#14233a" stroke-width="2"/></svg>
    <svg width="28" height="14" viewBox="0 0 28 14"><path d="M1 7h25M20 1l6 6-6 6" fill="none" stroke="#ec1c3a" stroke-width="2"/></svg>
  </div>
</section>

<section class="customers">
  <h2 class="heading">Some <span class="accent">customers</span> we support</h2>
  <div class="logos">
    <div class="logo-box">Corvana</div>
    <div class="logo-box">Telnexa</div>
    <div class="logo-box red">Shieldora</div>
    <div class="logo-box">Netbridge</div>
    <div class="logo-box">Fibrelyn</div>
  </div>
  <div class="arrows" style="left:572px;top:3084px">
    <svg width="24" height="14" viewBox="0 0 24 14"><path d="M23 7H2M8 1L2 7l6 6" fill="none" stroke="#14233a" stroke-width="2"/></svg>
    <svg width="28" height="14" viewBox="0 0 28 14"><path d="M1 7h25M20 1l6 6-6 6" fill="none" stroke="#ec1c3a" stroke-width="2"/></svg>
  </div>
</section>

<section class="res">
  <h2 class="heading">Helpful Resourses</h2>
  <article class="post" style="left:164px">
    <div class="thumb" role="img" aria-label="Cybersecurity lock graphic over a network of business icons" style="background:linear-gradient(135deg,#0b2a45,#1f7a8c)"></div>
    <div class="txt"><time>February 25, 2025</time><h3>Cybersecurity Training: An Essential Shield for Your Business</h3><p>Is Your Business a Cybersecurity Target? (Hint: Yes) One of the biggest misconceptions among...</p><a>Read More</a></div>
  </article>
  <article class="post" style="left:461px">
    <div class="thumb" role="img" aria-label="City skyline at dusk with connected network icons" style="background:linear-gradient(160deg,#2b5f8a,#6b90b0 50%,#c9874f)"></div>
    <div class="txt"><time>April 9, 2025</time><h3>The Importance of High-Speed, Stable Internet for SMBs</h3><p>Poor Connectivity Can Really Hurt Your Business's Digital Lifeline How much does your business...</p><a>Read More</a></div>
  </article>
  <article class="post" style="left:757px">
    <div class="thumb" role="img" aria-label="Hands typing on a laptop with email icons" style="background:linear-gradient(135deg,#e9eef3,#b9c7d5)"></div>
    <div class="txt"><time>April 2, 2025</time><h3>Inbox Blues? How to Fix Common Email Sending &amp; Receiving Issues</h3><p>How to Fix Sending and Receiving Issues Ever hit "send" only to wonder if your email vanished...</p><a>Read More</a></div>
  </article>
  <a class="btn abs" style="left:499px;top:3654px;width:202px">View All Resourses</a>
</section>

<section class="contact">
  <h2 class="heading">Looking for IT Support in Sydney?<br>Explore <span class="accent">Managed IT Support<br>Services</span> for Your Business</h2>
  <p class="body">Get help managing IT for your small or medium business from our team based right here in Sydney. Whether your team is working on-site or remotely, Velmora IT can help you streamline your operations. Contact us today to schedule a consultation and learn how we can support your business goals.</p>
  <form class="form">
    <h3 class="heading">Let's Talk</h3>
    <div class="field">Name</div>
    <div class="field">Company Name</div>
    <div class="field">Email Adderss</div>
    <div class="field">How Can We Help</div>
    <div class="field area"></div>
    <div class="submit">SUBMIT</div>
  </form>
</section>

<footer class="footer">
  <div class="brand">velmora</div>
  <div class="socials" aria-label="Social media links"><span></span><span></span><span></span></div>
  <div class="fcol" style="left:450px"><h4>About us</h4><ul><li>Our Company</li><li>Our Team</li><li>Velmora IT Partners</li><li>Contact Us</li></ul></div>
  <div class="fcol" style="left:659px"><h4>Useful links</h4><ul><li>Services</li><li>Blog</li><li>Videos</li><li>Huddle Chat</li></ul></div>
  <div class="fcol" style="left:872px"><h4>Our Solutions</h4><ul><li>IT Support</li><li>Project Management</li><li>IT Consulting and Training</li><li>Hardware and Software</li><li>IT Cyber Security</li><li>Cloud Solutions</li><li>IT Procurement and Auditing</li><li>Mobile and Web Development</li></ul></div>
  <div class="top-btn"><svg width="40" height="40" viewBox="0 0 40 40"><path d="M14 23l6-6 6 6" fill="none" stroke="#fff" stroke-width="2"/></svg></div>
  <div class="frule"></div>
  <div class="copy">© Copyright 2025 Velmora IT | All Rights Reserved</div>
</footer>

</body>
</html>
```